New local Orchid nursery branding

We need a business card designed for our small local company in Darwin, Australia that grows orchids, called Blooms at Carrow.
We will be running private sales from our property, and handing these out at local events for perspective customers.

We would like to see designs that are simple, and able to be used with minimal colours and containing an orchid, preferably a stylised representation instead of a photo.
The eventual hope is to take this into larger formats to create our company logo/branding etc, but for now we just need business cards.

Target Market(s)

Local Orchid

Industry/Entity Type

Business

Contact Information for Business Card

Company Name
Logo
Name
Phone Number
Street Address
Email Address (less prominent than rest of the text)

Font styles to use
Sans Serif

Requirements
Must have
• Name of the company, which is Blooms at Carrow
Nice to have
• stylised orchid logo
Should not have
• too many colours

```html
<!DOCTYPE html>
<html lang="en">
<head>
<meta charset="utf-8">
<title>Blooms at Carrow – Business Card</title>
<link rel="stylesheet" href="https://fonts.googleapis.com/css2?family=Arimo:wght@400;700&display=swap">
<style>
  :root {
    --card-bg: #ffffff;
    --brand-purple: #520050;
    --brand-blue: #3a4cb8;
    --ink: #000000;
    --icon-grey: #5a5a5a;
  }
  html, body {
    margin: 0;
    padding: 0;
    width: 1200px;
    height: 771px;
    overflow: hidden;
    background: var(--card-bg);
  }
  .card {
    position: relative;
    width: 1200px;
    height: 771px;
    background: var(--card-bg);
    font-family: "Arimo", Arial, sans-serif;
    color: var(--ink);
    overflow: hidden;
  }
  .sweep {
    position: absolute;
    inset: 0;
    width: 1200px;
    height: 771px;
  }
  .brand {
    position: absolute;
    left: 34px;
    top: 180px;
    display: flex;
    align-items: center;
    gap: 18px;
  }
  .brand-dot {
    width: 56px;
    height: 56px;
    border-radius: 50%;
    background: var(--brand-purple);
  }
  .brand-name {
    font-size: 52px;
    font-weight: 400;
    color: var(--brand-blue);
    letter-spacing: 1px;
    line-height: 1;
  }
  .person-name {
    position: absolute;
    left: 81px;
    top: 329px;
    margin: 0;
    font-size: 44px;
    font-weight: 700;
    line-height: 1;
  }
  .contact {
    position: absolute;
    left: 79px;
    top: 398px;
    margin: 0;
    padding: 0;
    list-style: none;
    font-size: 36px;
    line-height: 44px;
  }
  .contact li {
    display: flex;
    align-items: center;
  }
  .contact-icon {
    width: 50px;
    display: flex;
    align-items: center;
  }
  .address {
    position: absolute;
    left: 81px;
    top: 521px;
    margin: 0;
    font-style: normal;
    font-size: 35.5px;
    line-height: 42.7px;
  }
  .address .country {
    font-weight: 700;
  }
</style>
</head>
<body>
  <div class="card">
    <svg class="sweep" viewBox="0 0 1200 771" aria-hidden="true">
      <path d="M0,771 C450,720 900,420 1200,51 L1200,771 Z" fill="var(--brand-purple)"/>
    </svg>

    <div class="brand">
      <span class="brand-dot"></span>
      <span class="brand-name">Blooms at Carrow</span>
    </div>

    <h1 class="person-name">Name Here</h1>

    <ul class="contact">
      <li>
        <span class="contact-icon">
          <svg width="18" height="34" viewBox="0 0 18 34" aria-hidden="true">
            <rect x="12" y="0" width="2" height="6" fill="var(--icon-grey)"/>
            <rect x="1" y="5" width="16" height="28" rx="2" fill="var(--icon-grey)"/>
            <rect x="4" y="8" width="10" height="7" fill="#ffffff"/>
            <g fill="#ffffff">
              <rect x="4" y="18" width="2" height="2"/><rect x="8" y="18" width="2" height="2"/><rect x="12" y="18" width="2" height="2"/>
              <rect x="4" y="22" width="2" height="2"/><rect x="8" y="22" width="2" height="2"/><rect x="12" y="22" width="2" height="2"/>
              <rect x="4" y="26" width="2" height="2"/><rect x="8" y="26" width="2" height="2"/><rect x="12" y="26" width="2" height="2"/>
            </g>
          </svg>
        </span>
        <span>+61 000 000 000</span>
      </li>
      <li>
        <span class="contact-icon">
          <svg width="30" height="19" viewBox="0 0 30 19" aria-hidden="true">
            <rect x="0.75" y="0.75" width="28.5" height="17.5" fill="none" stroke="var(--icon-grey)" stroke-width="1.5"/>
            <path d="M1,1 L15,11 L29,1 M1,18 L11,8.5 M29,18 L19,8.5" fill="none" stroke="var(--icon-grey)" stroke-width="1.5"/>
          </svg>
        </span>
        <span>emailaddresshere@email.com</span>
      </li>
    </ul>

    <address class="address">
      100 Sample Street<br>
      Pellin, RK<br>
      <span class="country">Australia</span>
    </address>
  </div>
</body>
</html>
```